Facebook Fan Page for Kestro Vane, EDM DJ!

I just got a new logo because I plan a reboot in my DJ Career. This also includes a new visual identity in all categories. So in social media. I need a title picture and a profile pic which represent my alias as EDM-DJ. Both should be usable in facebook and twitter as well. It can not be necessary. The graphics should represent my favorite music styles in EDM for example: House, Electro, Electro House, Melbourne Bounce and Big Room. The design should match the new logo which I attached to the project description.

Target Market(s)

Young people who love electronic music and DJ mixes.

Industry/Entity Type

Media

Colors

Designer to choose colors to be used in the design.

Requirements
Must have
• I definitely need graphics to represent my logo and what I'm doing. It should be fit together.
Nice to have
• Complete background design for the facebook and twitter page. Nice to have but not necessary. Maybe implied dj gear in an abstract way.
Should not have
• Funny pictures and a playful or childish appearance. No golden elements.

```html
<!DOCTYPE html>
<html lang="en">
<head>
<meta charset="utf-8">
<title>Kestro Vane – Social Profile Set</title>
<link rel="stylesheet" href="https://fonts.googleapis.com/css2?family=Roboto:ital,wght@0,400;0,900;1,500&display=swap">
<style>
  :root {
    --page-bg: #e9ebee;
    --ink-black: #000000;
    --brand-blue: #1f7bd1;
    --text-white: #ffffff;
    --stage-purple: #3a1656;
    --stage-magenta: #d8348f;
    --stage-cyan: #29c6e0;
    --stage-lime: #8fd14a;
  }
  * { box-sizing: border-box; margin: 0; padding: 0; }
  html, body {
    width: 1200px;
    height: 750px;
    overflow: hidden;
    background: var(--page-bg);
    font-family: "Roboto", Arial, sans-serif;
  }
  .artboard {
    position: relative;
    width: 1200px;
    height: 750px;
  }
  .profile-picture {
    position: absolute;
    left: 85px;
    top: 218px;
    width: 181px;
    height: 181px;
    background: var(--ink-black);
    display: flex;
    flex-direction: column;
    align-items: center;
    justify-content: center;
    gap: 10px;
  }
  .profile-picture .brand-dot {
    width: 46px;
    height: 46px;
    border-radius: 50%;
    background: var(--brand-blue);
  }
  .profile-picture .brand-initials {
    color: var(--brand-blue);
    font-weight: 900;
    font-size: 68px;
    line-height: 1;
    letter-spacing: 2px;
  }
  .cover-photo {
    position: absolute;
    left: 278px;
    top: 217px;
    width: 817px;
    height: 314px;
    background: var(--ink-black);
    overflow: hidden;
  }
  .cover-scene {
    position: absolute;
    inset: 0 0 80px 0;
    background:
      radial-gradient(ellipse 30% 55% at 22% 45%, var(--stage-magenta) 0%, transparent 70%),
      radial-gradient(ellipse 25% 50% at 45% 40%, var(--stage-lime) 0%, transparent 70%),
      radial-gradient(ellipse 35% 60% at 70% 35%, var(--stage-cyan) 0%, transparent 70%),
      radial-gradient(ellipse 30% 50% at 90% 30%, var(--stage-magenta) 0%, transparent 75%),
      linear-gradient(180deg, var(--stage-purple) 0%, #1a0a2a 100%);
  }
  .cover-scene::after {
    content: "";
    position: absolute;
    inset: 0;
    background: linear-gradient(180deg, transparent 55%, var(--ink-black) 100%);
  }
  .contact-list {
    position: absolute;
    left: 28px;
    top: 69px;
    list-style: none;
    top: 69px;
  }
  .contact-list { top: auto; bottom: 32px; }
  .contact-item {
    display: flex;
    align-items: center;
    gap: 8px;
    color: var(--brand-blue);
    font-style: italic;
    font-weight: 500;
  }
  .contact-item.phone { font-size: 25px; }
  .contact-item.email { font-size: 17px; margin-top: 4px; }
  .contact-item .at-sign {
    color: var(--text-white);
    font-style: normal;
    font-weight: 900;
    font-size: 18px;
    width: 18px;
  }
  .brand-lockup {
    position: absolute;
    right: 24px;
    top: 242px;
    display: flex;
    align-items: center;
    gap: 12px;
  }
  .brand-lockup .brand-dot {
    width: 30px;
    height: 30px;
    border-radius: 50%;
    background: var(--brand-blue);
  }
  .brand-lockup .brand-name {
    color: var(--brand-blue);
    font-weight: 900;
    font-size: 38px;
    letter-spacing: 1px;
    line-height: 1;
  }
</style>
</head>
<body>
  <main class="artboard">
    <div class="profile-picture">
      <span class="brand-dot"></span>
      <span class="brand-initials">KV</span>
    </div>

    <section class="cover-photo">
      <div class="cover-scene" role="img" aria-label="Photo of a DJ at turntables with a cheering crowd under colourful club lights"></div>

      <ul class="contact-list">
        <li class="contact-item phone">
          <svg width="18" height="18" viewBox="0 0 24 24" aria-hidden="true">
            <path fill="#ffffff" d="M6.6 10.8a15.1 15.1 0 0 0 6.6 6.6l2.2-2.2c.3-.3.7-.4 1-.2 1.1.4 2.3.6 3.6.6.6 0 1 .4 1 1V20c0 .6-.4 1-1 1A17 17 0 0 1 3 4c0-.6.4-1 1-1h3.5c.6 0 1 .4 1 1 0 1.3.2 2.5.6 3.6.1.3 0 .7-.2 1z"/>
          </svg>
          <span>555 014 2738</span>
        </li>
        <li class="contact-item email">
          <span class="at-sign">@</span>
          <span>kestro@vanemix.com</span>
        </li>
      </ul>

      <div class="brand-lockup">
        <span class="brand-dot"></span>
        <span class="brand-name">KESTRO VANE</span>
      </div>
    </section>
  </main>
</body>
</html>
```